Succession & Estate Planning firm needs a double-sided one page client handout

We need a client hand-out that highlights the top 10 Reasons to get a Pension Plan. It will need the 10 reasons as headings, with a short description of each reason (attached Word doc). It should communicate that a Pension Plan is flexible and provides security. Our usual client is a business owner/medical professional/entrepreneur. Have a look at our website for more info about our business www.marvelko.ca Our logo colours are 83c242, 3b3839, d5d5d5 We like clean, modern, info-graphics, not too cluttered, not too loudWe would like the ability to update the text/content ourselves, in the future.

```html
<!DOCTYPE html>
<html lang="en">
<head>
<meta charset="utf-8">
<title>Top 10 Benefits of a Family Pension Plan – Marvelko</title>
<link href="https://fonts.googleapis.com/css2?family=Bebas+Neue&family=Jost:wght@400;500&display=swap" rel="stylesheet">
<style>
:root{
  --green:#83c242;
  --charcoal:#3b3839;
  --grey:#d5d5d5;
  --stage:#e4e4e5;
  --text:#2f2d2e;
  --mint:#e3f2d0;
}
*{box-sizing:border-box;margin:0;padding:0}
html,body{width:1200px;height:859px;overflow:hidden}
body{background:var(--stage);position:relative;font-family:'Jost',sans-serif;color:var(--text)}
.sheet{position:absolute;top:111px;width:497px;height:641px;overflow:hidden;box-shadow:0 6px 14px rgba(0,0,0,.18)}
.sheet--front{left:85px;background:linear-gradient(#fff 52%,var(--mint) 100%)}
.sheet--back{left:630px;background:linear-gradient(var(--mint) 0%,#fff 16%,#fff 78%,var(--mint) 100%)}
.hero{position:absolute;left:0;top:0;width:497px;height:243px;
  background:
   linear-gradient(180deg,rgba(0,0,0,0) 68%,#5a4331 84%,#3a2a1e 100%),
   radial-gradient(circle at 20% 25%,#fdfbe6 0%,#eef3b8 28%,rgba(200,220,90,0) 55%),
   linear-gradient(90deg,#d8e48a 0%,#9cc94a 45%,#3f7d26 100%)}
.brand{position:absolute;left:24px;top:38px;display:flex;align-items:center;gap:7px}
.brand__name{font-family:'Jost',sans-serif;font-weight:400;font-size:24px;letter-spacing:4px;color:var(--charcoal)}
.brand__dot{width:11px;height:11px;border-radius:50%;background:var(--green)}
.title-band{position:absolute;left:0;top:243px;width:497px;height:45px;background:var(--charcoal);
  display:flex;align-items:center;justify-content:center}
.title{font-family:'Bebas Neue',sans-serif;font-weight:400;font-size:32px;line-height:1;letter-spacing:.2px;color:#fff;white-space:nowrap}
.title em{font-style:normal;color:var(--green)}
.sheet--back .title{position:absolute;left:45px;top:24px;color:var(--charcoal);font-size:33px}
.benefit{position:absolute;left:43px;width:420px}
.benefit__num{position:absolute;left:0;top:0;width:24px;height:24px;border-radius:50%;background:var(--green);
  color:#fff;font-size:11px;font-weight:500;display:flex;align-items:center;justify-content:center}
.benefit__head{position:absolute;left:40px;top:-4px;font-size:11.5px;font-weight:500;color:var(--green);white-space:nowrap}
.benefit__body{position:absolute;left:40px;top:20px;width:315px;font-size:8.6px;line-height:1.35}
.benefit__icon{position:absolute;left:365px;top:-8px;width:48px;height:48px}
.benefit__icon svg{width:48px;height:48px;fill:none;stroke:var(--charcoal);stroke-width:2.2;stroke-linecap:round;stroke-linejoin:round}
.benefit__icon .g{stroke:var(--green)}
.contact-bar{position:absolute;left:0;bottom:0;width:497px;height:41px;background:var(--charcoal);
  display:flex;align-items:center;justify-content:center;gap:20px;color:#fff;font-size:8.6px}
.contact-bar span{display:flex;align-items:center;gap:6px;white-space:nowrap}
.contact-bar svg{width:14px;height:14px;fill:var(--green)}
</style>
</head>
<body>

<section class="sheet sheet--front">
  <div class="hero" role="img" aria-label="Photo of young seedlings growing from stacks of coins in soil, glowing green background"></div>
  <div class="brand"><span class="brand__name">MARVELKO</span><span class="brand__dot"></span></div>
  <div class="title-band"><h1 class="title"><em>Top 10 Benefits</em> of a Family Pension Plan</h1></div>

  <div class="benefit" style="top:308px">
    <div class="benefit__num">1</div>
    <h2 class="benefit__head">Create Significant Deductions</h2>
    <p class="benefit__body">The FPP creates significant tax deductions, which can be used to keep the business under the small business rate or applied to the high rate.</p>
    <div class="benefit__icon"><svg viewBox="0 0 48 48"><path d="M10 6h20l8 8v28H10z"/><path d="M30 6v8h8"/><rect class="g" x="14" y="14" width="18" height="10"/><path d="M15 30h16M15 35h12"/><path class="g" d="M44 24L30 40l-4 2 1-4 14-16z"/></svg></div>
  </div>

  <div class="benefit" style="top:381px">
    <div class="benefit__num">2</div>
    <h2 class="benefit__head">Deliberate. Planned. Future Income</h2>
    <p class="benefit__body">An income for beyond the last day at the office.</p>
    <div class="benefit__icon"><svg viewBox="0 0 48 48"><rect class="g" x="22" y="6" width="22" height="20"/><path class="g" d="M22 12h22M27 4v4M39 4v4"/><circle cx="14" cy="20" r="6"/><path d="M4 42c0-8 4-12 10-12s10 4 10 12z"/><path d="M30 32h14M30 37h14M30 42h14"/></svg></div>
  </div>

  <div class="benefit" style="top:442px">
    <div class="benefit__num">3</div>
    <h2 class="benefit__head">Past Buy Back</h2>
    <p class="benefit__body">Most owners invest in their business first. The FPP offers the ability to go back and recover lost years when RRSP contributions were not made and pass the tax savings on to their company.</p>
    <div class="benefit__icon"><svg viewBox="0 0 48 48"><path d="M10 14a18 18 0 1 1-2 20"/><path d="M10 6v8h8"/><path class="g" d="M26 14v11l6 5"/><path class="g" d="M6 36h12M6 41h12"/></svg></div>
  </div>

  <div class="benefit" style="top:522px">
    <div class="benefit__num">4</div>
    <h2 class="benefit__head">Creditor Proof</h2>
    <p class="benefit__body">All assets in an FPP are creditor proof. Planned pension contributions receive “super-priority” status, which ranks above the claims of secured creditors like major commercial lenders and banks.</p>
    <div class="benefit__icon"><svg viewBox="0 0 48 48"><circle class="g" cx="24" cy="16" r="9"/><path class="g" d="M24 11v10"/><path d="M4 14l4 16 10 12M44 14l-4 16-10 12"/><path d="M12 26l8 8M36 26l-8 8"/></svg></div>
  </div>

  <footer class="contact-bar">
    <span><svg viewBox="0 0 16 16"><path d="M8 1l7 6h-2v8H9v-5H7v5H3V7H1z"/></svg>410 – 88 Harbour Avenue, Regina SK S4P 2B1</span>
    <span><svg viewBox="0 0 16 16"><path d="M3 1l3 3-2 2c1 2 3 4 5 5l2-2 3 3-2 3C6 15 1 10 1 3z"/></svg>306-555-0148</span>
    <span><svg viewBox="0 0 16 16"><path d="M8 1a7 7 0 1 0 0 14A7 7 0 0 0 8 1zm0 1.5c.9 1 1.5 2.7 1.6 4.7H6.4C6.5 5.2 7.1 3.5 8 2.5zM2.6 7.2A5.5 5.5 0 0 1 5.6 3c-.5 1.2-.8 2.6-.8 4.2zm0 1.6h2.2c0 1.6.3 3 .8 4.2a5.5 5.5 0 0 1-3-4.2zm3.8 0h3.2c-.1 2-.7 3.7-1.6 4.7-.9-1-1.5-2.7-1.6-4.7zm5 0h2a5.5 5.5 0 0 1-3 4.2c.6-1.2.9-2.6 1-4.2zm0-1.6c0-1.6-.4-3-1-4.2a5.5 5.5 0 0 1 3 4.2z"/></svg>marvelko.ca</span>
  </footer>
</section>

<section class="sheet sheet--back">
  <h1 class="title"><em>Top 10 Benefits</em> of a Family Pension Plan</h1>

  <div class="benefit" style="top:84px">
    <div class="benefit__num">5</div>
    <h2 class="benefit__head">Flexibility</h2>
    <p class="benefit__body">Owners know that cash flows can swing wildly with the business cycle. An FPP offers the flexibility to flip between DB and DC accounts to conserve cash, smooth income during volatile years, and recover assets when profits improve.</p>
    <div class="benefit__icon"><svg viewBox="0 0 48 48"><path class="g" d="M24 4v40M18 10l6-6 6 6"/><path d="M24 30c0-8-6-12-16-12M12 12l-6 6 6 6M24 30c0-8 6-12 16-12M36 12l6 6-6 6"/></svg></div>
  </div>

  <div class="benefit" style="top:174px">
    <div class="benefit__num">6</div>
    <h2 class="benefit__head">Preserve the Lifetime Capital Gains Exemption</h2>
    <p class="benefit__body">Create $1.6 Million+ of Tax Free Capital Gains. The significant deductions created in an FPP can be used to purify a corporation with passive assets, which can help preserve the shareholders’ lifetime capital gains exemption.</p>
    <div class="benefit__icon"><svg viewBox="0 0 48 48"><path class="g" d="M20 6h8l-2 5c6 3 8 8 8 12 0 4-4 6-10 6s-10-2-10-6c0-4 2-9 8-12z"/><path class="g" d="M27 16h-4a2 2 0 0 0 0 4h2a2 2 0 0 1 0 4h-4M24 14v12"/><path d="M4 32h4v10H4M8 34h10l8 2h10c4 0 6-2 8-4M8 42h22"/></svg></div>
  </div>

  <div class="benefit" style="top:264px">
    <div class="benefit__num">7</div>
    <h2 class="benefit__head">Intergenerational Wealth Transfer</h2>
    <p class="benefit__body">Unlike RRSPs that eventually trigger a taxable disposition upon death, an FPP has the ability to pass, tax deferred, to the next generation of family business owners.</p>
    <div class="benefit__icon"><svg viewBox="0 0 48 48"><rect x="6" y="16" width="36" height="16" stroke-width="3"/><path d="M27 20h-4a2 2 0 0 0 0 4h2a2 2 0 0 1 0 4h-4M24 18v12"/><path class="g" d="M14 10a14 14 0 0 1 22 2M36 6v6h-6M34 38a14 14 0 0 1-22-2M12 42v-6h6"/></svg></div>
  </div>

  <div class="benefit" style="top:341px">
    <div class="benefit__num">8</div>
    <h2 class="benefit__head">All Ages</h2>
    <p class="benefit__body">An FPP can benefit all entrepreneurs between ages 18-71.</p>
    <div class="benefit__icon"><svg viewBox="0 0 48 48"><circle cx="8" cy="30" r="4"/><circle class="g" cx="24" cy="22" r="6"/><circle cx="40" cy="14" r="8"/><path d="M4 42h40"/></svg></div>
  </div>

  <div class="benefit" style="top:400px">
    <div class="benefit__num">9</div>
    <h2 class="benefit__head">Conserve the Small Business Deduction</h2>
    <p class="benefit__body">Investment income inside an FPP grows tax exempt and does not create passive income. Business owners that redirect corporate resources to fund their pension assets will not jeopardize their low corporate tax rate on profits and in associated companies.</p>
    <div class="benefit__icon"><svg viewBox="0 0 48 48"><path d="M4 22a20 16 0 0 1 40 0zM24 6v36"/><path d="M14 22l10-16 10 16"/><circle class="g" cx="12" cy="34" r="5"/><circle class="g" cx="36" cy="34" r="5"/></svg></div>
  </div>

  <div class="benefit" style="top:501px">
    <div class="benefit__num">10</div>
    <h2 class="benefit__head">Broader Investment Options</h2>
    <p class="benefit__body">An FPP allows entrepreneurs to invest in what they like: real estate, other businesses and/or franchises, private equity, public equity, exempt markets, etc.</p>
    <div class="benefit__icon"><svg viewBox="0 0 48 48"><path class="g" d="M4 26l12-10 8 8 18-16M34 8h8v8"/><path d="M8 44V34M16 44V28M24 44V32M32 44V24M40 44V18" stroke-width="3"/></svg></div>
  </div>

  <footer class="contact-bar">
    <span><svg viewBox="0 0 16 16"><path d="M8 1l7 6h-2v8H9v-5H7v5H3V7H1z"/></svg>410 – 88 Harbour Avenue, Regina SK S4P 2B1</span>
    <span><svg viewBox="0 0 16 16"><path d="M3 1l3 3-2 2c1 2 3 4 5 5l2-2 3 3-2 3C6 15 1 10 1 3z"/></svg>306-555-0148</span>
    <span><svg viewBox="0 0 16 16"><path d="M8 1a7 7 0 1 0 0 14A7 7 0 0 0 8 1zm0 1.5c.9 1 1.5 2.7 1.6 4.7H6.4C6.5 5.2 7.1 3.5 8 2.5zM2.6 7.2A5.5 5.5 0 0 1 5.6 3c-.5 1.2-.8 2.6-.8 4.2zm0 1.6h2.2c0 1.6.3 3 .8 4.2a5.5 5.5 0 0 1-3-4.2zm3.8 0h3.2c-.1 2-.7 3.7-1.6 4.7-.9-1-1.5-2.7-1.6-4.7zm5 0h2a5.5 5.5 0 0 1-3 4.2c.6-1.2.9-2.6 1-4.2zm0-1.6c0-1.6-.4-3-1-4.2a5.5 5.5 0 0 1 3 4.2z"/></svg>marvelko.ca</span>
  </footer>
</section>

</body>
</html>
```